Business Card

Can you please copy the format provided for the business cards.
Can the logo be in the colours of the last file as specified.

Can the text please be in grey

• Navy Blue: #00457C
• Grey Text: #555555
• Orange Text: #FDBF29

The names on the business card will be

Dorian Platt
0452 718 340
dorian.platt@ridgelineassetlending.com.au

Lvl 7, 14 Harbourview Pde
Merrivale QLD 4290
PO Box 3472
Tarrin Vale MC QLD 9781
P: 1300 462 519
F: 1300 462 538
www.ridgelineassetlending.com.au

And

Liam Hollis
0437 915 604
liam.hollis@ridgelineassetlending.com.au

Lvl 7, 14 Harbourview Pde
Merrivale QLD 4290
PO Box 3472
Tarrin Vale MC QLD 9781
P: 1300 462 519
F: 1300 471 926

Industry/Entity Type

Business

```html
<!DOCTYPE html>
<html lang="en">
<head>
<meta charset="utf-8">
<title>Ridgeline Asset Lending – Business Cards</title>
<link rel="stylesheet" href="https://fonts.googleapis.com/css2?family=Lato:wght@400;700;900&display=swap">
<style>
  :root {
    --navy: #00457C;
    --navy-band: #13477A;
    --grey-text: #555555;
    --orange: #FDBF29;
    --white: #FFFFFF;
    --stage: #2B2B2B;
    --rule: #9A9A9A;
  }
  * { margin: 0; padding: 0; box-sizing: border-box; }
  html, body { width: 1200px; height: 926px; overflow: hidden; }
  body {
    background: var(--stage);
    font-family: "Lato", Arial, sans-serif;
    position: relative;
  }
  .card {
    position: absolute;
    width: 508px;
    height: 328px;
    background: var(--white);
    overflow: hidden;
    box-shadow: 0 2px 10px rgba(0,0,0,0.45);
  }
  .card--front-1 { left: 80px; top: 110px; }
  .card--back-1  { left: 625px; top: 110px; }
  .card--front-2 { left: 80px; top: 478px; }
  .card--back-2  { left: 625px; top: 478px; }

  /* Front */
  .brand {
    position: absolute;
    display: flex;
    align-items: center;
    gap: 12px;
  }
  .brand__mark {
    width: 34px; height: 34px;
    background: var(--navy);
  }
  .brand__name {
    color: var(--navy);
    font-weight: 900;
    text-transform: uppercase;
    line-height: 1.05;
    letter-spacing: 0.5px;
  }
  .front .brand { left: 50%; top: 56px; transform: translateX(-50%); }
  .front .brand__name { font-size: 19px; }

  .tagline-band {
    position: absolute;
    left: 0; top: 168px;
    width: 100%; height: 28px;
    background: var(--orange);
    display: flex; align-items: center; justify-content: center;
    font-size: 19px;
    letter-spacing: 3px;
    color: #111;
    white-space: nowrap;
  }
  .tagline-band strong { font-weight: 900; }

  .contact-panel {
    position: absolute;
    left: 0; top: 196px;
    width: 100%; height: 132px;
    background: var(--navy-band);
    color: var(--white);
    padding: 27px 0 0 37px;
  }
  .contact-panel__name { font-size: 23px; font-weight: 700; line-height: 1.2; }
  .contact-panel__phone { font-size: 19px; line-height: 1.35; }
  .contact-panel__email { font-size: 14px; line-height: 1.7; }

  /* Back */
  .back .brand { left: 26px; top: 148px; gap: 9px; }
  .back .brand__mark { width: 26px; height: 26px; }
  .back .brand__name { font-size: 13px; }
  .back__details {
    position: absolute;
    left: 194px; top: 94px;
    border-left: 1px solid var(--rule);
    padding-left: 10px;
    color: var(--grey-text);
    font-size: 15px;
    line-height: 19.7px;
    white-space: nowrap;
  }
</style>
</head>
<body>

  <section class="card card--front-1 front" aria-label="Business card front, Dorian Platt">
    <div class="brand"><span class="brand__mark"></span><span class="brand__name">Ridgeline<br>Asset Lending</span></div>
    <div class="tagline-band">Backing&nbsp;<strong>Assets</strong>&nbsp;Building&nbsp;<strong>Futures</strong></div>
    <div class="contact-panel">
      <p class="contact-panel__name">Dorian Platt</p>
      <p class="contact-panel__phone">0452 718 340</p>
      <p class="contact-panel__email">dorian.platt@ridgelineassetlending.com.au</p>
    </div>
  </section>

  <section class="card card--back-1 back" aria-label="Business card back, office details">
    <div class="brand"><span class="brand__mark"></span><span class="brand__name">Ridgeline<br>Asset Lending</span></div>
    <div class="back__details">
      <p>Lvl 7, 14 Harbourview Pde</p>
      <p>Merrivale QLD 4290</p>
      <p>PO Box 3472</p>
      <p>Tarrin Vale MC QLD 9781</p>
      <p>P: 1300 462 519</p>
      <p>F: 1300 462 538</p>
      <p>www.ridgelineassetlending.com.au</p>
    </div>
  </section>

  <section class="card card--front-2 front" aria-label="Business card front, Liam Hollis">
    <div class="brand"><span class="brand__mark"></span><span class="brand__name">Ridgeline<br>Asset Lending</span></div>
    <div class="tagline-band">Backing&nbsp;<strong>Assets</strong>&nbsp;Building&nbsp;<strong>Futures</strong></div>
    <div class="contact-panel">
      <p class="contact-panel__name">Liam Hollis</p>
      <p class="contact-panel__phone">0437 915 604</p>
      <p class="contact-panel__email">liam.hollis@ridgelineassetlending.com.au</p>
    </div>
  </section>

  <section class="card card--back-2 back" aria-label="Business card back, office details">
    <div class="brand"><span class="brand__mark"></span><span class="brand__name">Ridgeline<br>Asset Lending</span></div>
    <div class="back__details">
      <p>Lvl 7, 14 Harbourview Pde</p>
      <p>Merrivale QLD 4290</p>
      <p>PO Box 3472</p>
      <p>Tarrin Vale MC QLD 9781</p>
      <p>P: 1300 462 519</p>
      <p>F: 1300 471 926</p>
      <p>www.ridgelineassetlending.com.au</p>
    </div>
  </section>

</body>
</html>
```